Business card for a boutique travel agency VELARIEN

we need a business card design - double sided. We would like to have a very elegant, sophisticated but modern design. we are travel consultants and our business focus is Europe, mainly the city of Paris. We would like to receive designs in white and silver, black color but if you are confident that we should pick up a color to make it different and more beautful...go ahead! We are going to give business cards to our clients and business partners. It is important to be perceived as elegant, modern and trustful. Please check jpg references.

Target Market(s)

Velarien primary clients are individuals, couples and affinity groups of high-net-worth who travel for leisure at least once per year. Seeking the ultimate travel experience, the target clients demand the finest quality activities and accommodations accompanied by a superior level of service.

Industry/Entity Type

Travel Industry

Contact Information for Business Card

Lucinda Farrow
- lucinda@velarien-example.com
- +55 11 98347.2516
- velarien-example.com
- unique travel experiences (we would like to see this signature printed as a detail)

Font styles to use
Sans Serif

Colors

Designer to choose colors to be used in the design.

Requirements
Must have
• the Velarien logo that I have attached
Nice to have
• we would like to have some nice detail, something different that shows that we care about,... we are detail oriented.
Should not have
• decorative fonts

```html
<!DOCTYPE html>
<html lang="en">
<head>
<meta charset="utf-8">
<title>Velarien — Business Card</title>
<link href="https://fonts.googleapis.com/css2?family=Josefin+Sans:wght@300&family=Roboto:wght@400;700&family=Roboto+Condensed:wght@700&display=swap" rel="stylesheet">
<style>
  :root {
    --backdrop: #e6eaea;
    --card-black: #141414;
    --card-white: #f4f4f4;
    --ink-light: #ffffff;
    --ink-dark: #161616;
    --divider: #9a9a9a;
  }
  * { box-sizing: border-box; margin: 0; padding: 0; }
  html, body { width: 1200px; height: 900px; overflow: hidden; }
  body {
    background: var(--backdrop);
    display: flex;
    flex-direction: column;
    align-items: center;
    justify-content: center;
    gap: 44px;
  }
  .card {
    width: 660px;
    height: 378px;
    position: relative;
    box-shadow: 0 10px 28px rgba(0,0,0,0.12);
  }
  .card--front {
    background: var(--card-black);
    color: var(--ink-light);
    display: flex;
    flex-direction: column;
    align-items: center;
    justify-content: center;
  }
  .wordmark {
    font-family: "Josefin Sans", sans-serif;
    font-weight: 300;
    letter-spacing: 0.42em;
    text-transform: uppercase;
    padding-left: 0.42em;
  }
  .card--front .wordmark { font-size: 40px; }
  .tagline {
    position: absolute;
    bottom: 70px;
    left: 0; right: 0;
    text-align: center;
    font-family: "Roboto", sans-serif;
    font-weight: 700;
    font-size: 15px;
    letter-spacing: 0.03em;
  }
  .card--back {
    background: var(--card-white);
    color: var(--ink-dark);
    display: flex;
    align-items: center;
  }
  .card--back .wordmark {
    font-size: 27px;
    width: 330px;
    text-align: center;
    padding-left: 30px;
  }
  .divider {
    width: 1px;
    height: 112px;
    background: var(--divider);
    margin: 0 24px 0 6px;
  }
  .contact { font-family: "Roboto", sans-serif; }
  .contact__name {
    font-family: "Roboto Condensed", sans-serif;
    font-weight: 700;
    font-size: 22px;
    text-transform: uppercase;
    margin-bottom: 8px;
  }
  .contact__line {
    display: flex;
    align-items: center;
    gap: 8px;
    font-size: 13.5px;
    line-height: 1.45;
    color: #333;
  }
  .contact__line svg { width: 11px; height: 11px; flex: none; fill: var(--ink-dark); }
</style>
</head>
<body>
  <section class="card card--front">
    <div class="wordmark">Velarien</div>
    <p class="tagline">unique travel experiences</p>
  </section>

  <section class="card card--back">
    <div class="wordmark">Velarien</div>
    <div class="divider"></div>
    <div class="contact">
      <p class="contact__name">Lucinda Farrow</p>
      <p class="contact__line">
        <svg viewBox="0 0 24 24" aria-hidden="true"><path d="M6.6 10.8a15.2 15.2 0 0 0 6.6 6.6l2.2-2.2a1 1 0 0 1 1-.25 11.4 11.4 0 0 0 3.6.57 1 1 0 0 1 1 1V20a1 1 0 0 1-1 1A17 17 0 0 1 3 4a1 1 0 0 1 1-1h3.5a1 1 0 0 1 1 1c0 1.25.2 2.45.57 3.57a1 1 0 0 1-.25 1z"/></svg>
        +55 11 98347.2516
      </p>
      <p class="contact__line">
        <svg viewBox="0 0 24 24" aria-hidden="true"><path d="M2 5h20v14H2z M2 5l10 8 10-8" stroke="#f4f4f4" stroke-width="1.5"/></svg>
        lucinda@velarien-example.com
      </p>
      <p class="contact__line">
        <svg viewBox="0 0 24 24" aria-hidden="true"><circle cx="12" cy="12" r="10"/></svg>
        www.velarien-example.com
      </p>
    </div>
  </section>
</body>
</html>
```